New SKINCARE Label Design Project

Check out our website www.morleneglow.com. We offer a few products that are all natural, from drinks to skincare. We have new packaging for the "Dewbrin Balm" and need a new label design. We'd like out of the box thinking, but it should fit the existing concept. The product label should contain cool words, can be creative and should contain ingredients as this is a regulation.

I have added some examples of what we’d like. Please base your design on this.

Target Market(s)

skincare, cosmetics, natural, cool, young

Industry/Entity Type

Skin Care Product

Requirements
Must have
• Label must fit the existing concept, but should be out of the box, potentially using unexpected colors... Clean design, clean fonts, very professional, but playful at the same time, can maybe include cartoons, stars,...
Nice to have
• Out of the box thinking, we'd like to stand out from all other brands by label design, it should catch the eye and interest people to buy our product.

```html
<!DOCTYPE html>
<html lang="nl">
<head>
<meta charset="utf-8">
<title>Dewbrin Balm – tube label</title>
<link rel="stylesheet" href="https://fonts.googleapis.com/css2?family=Montserrat:wght@300;400&display=swap">
<style>
  :root {
    --canvas: #f3f0e8;
    --label-white: #ffffff;
    --olive: #bbb06e;
    --gold-soft: #e6d6ae;
    --lavender: #cdb8e6;
    --lavender-deep: #a98fcf;
    --ink-light: #ffffff;
    --ink-muted: #fbf8ee;
  }
  * { box-sizing: border-box; margin: 0; padding: 0; }
  html, body {
    width: 1180px;
    height: 1200px;
    overflow: hidden;
    background: var(--canvas);
  }
  .canvas {
    position: relative;
    width: 1180px;
    height: 1200px;
  }
  .label {
    position: absolute;
    left: 390px;
    top: 50px;
    width: 400px;
    height: 1100px;
    background: var(--label-white);
    overflow: hidden;
    box-shadow: 0 2px 18px rgba(120, 105, 60, 0.12);
    font-family: "Montserrat", sans-serif;
    color: var(--ink-light);
  }
  .label__band,
  .label__sparkles {
    position: absolute;
    inset: 0;
    width: 400px;
    height: 1100px;
  }
  .label__ornament {
    position: absolute;
    background: var(--gold-soft);
    border-radius: 6px;
  }
  .label__ornament--top {
    left: 50px;
    top: 40px;
    width: 300px;
    height: 230px;
  }
  .label__ornament--bottom {
    left: 160px;
    top: 1000px;
    width: 240px;
    height: 100px;
    border-radius: 6px 0 0 0;
  }
  .label__title {
    position: absolute;
    left: 0;
    right: 0;
    top: 335px;
    text-align: center;
    font-weight: 300;
    font-size: 50px;
    line-height: 1.2;
    letter-spacing: 0.12em;
    text-transform: uppercase;
  }
  .label__claims {
    position: absolute;
    left: 72px;
    right: 10px;
    top: 555px;
    list-style: none;
    font-weight: 300;
    font-size: 19px;
    line-height: 1.36;
    letter-spacing: 0.1em;
    text-transform: uppercase;
  }
  .label__claims li {
    position: relative;
    padding-left: 20px;
  }
  .label__claims li::before {
    content: "-";
    position: absolute;
    left: 0;
  }
  .label__ingredients {
    position: absolute;
    left: 72px;
    right: 40px;
    top: 800px;
    font-weight: 300;
    font-size: 11px;
    line-height: 1.5;
    letter-spacing: 0.06em;
    color: var(--ink-muted);
  }
  .label__ingredients-title {
    font-weight: 400;
    letter-spacing: 0.16em;
    text-transform: uppercase;
    margin-bottom: 2px;
  }
  .label__volume {
    position: absolute;
    left: 0;
    right: 0;
    top: 905px;
    text-align: center;
    font-weight: 300;
    font-size: 26px;
    letter-spacing: 0.1em;
  }
</style>
</head>
<body>
  <main class="canvas">
    <section class="label" aria-label="Dewbrin Balm tube label">
      <svg class="label__band" viewBox="0 0 400 1100" aria-hidden="true">
        <polygon points="0,300 400,220 400,985 0,1060" fill="var(--olive)"/>
      </svg>

      <div class="label__ornament label__ornament--top" role="img" aria-label="Gold line-art leaf pattern"></div>

      <svg class="label__sparkles" viewBox="0 0 400 1100" aria-hidden="true">
        <polygon points="352,300 357,313 370,318 357,323 352,336 347,323 334,318 347,313" fill="var(--lavender)"/>
        <polygon points="40,505 43,513 51,516 43,519 40,527 37,519 29,516 37,513" fill="var(--lavender)"/>
        <polygon points="345,900 349,910 359,914 349,918 345,928 341,918 331,914 341,910" fill="var(--lavender-deep)"/>
        <circle cx="60" cy="960" r="4" fill="var(--lavender)"/>
        <circle cx="330" cy="520" r="3" fill="var(--lavender)"/>
      </svg>

      <h1 class="label__title">Dewbrin<br>Balm</h1>

      <ul class="label__claims">
        <li>Voedt en beschermt<br>de huid.</li>
        <li>Ruwe huid wordt<br>zacht en glad.</li>
        <li>Vertraagt de<br>veroudering<br>van de huid.</li>
      </ul>

      <div class="label__ingredients">
        <p class="label__ingredients-title">Ingrediënten</p>
        <p>Aqua, Butyrospermum Parkii Butter, Glycerin, Simmondsia Chinensis Oil, Lavandula Angustifolia Oil, Tocopherol, Aloe Barbadensis Leaf Juice.</p>
      </div>

      <p class="label__volume">100ML</p>

      <div class="label__ornament label__ornament--bottom" role="img" aria-label="Gold line-art leaf pattern"></div>
    </section>
  </main>
</body>
</html>
```